High end business card design for custom homebuilding company

Looking for a high end business card design that is unique and elegant. Can use embossing, foil printing, laser die cutting, or any high end printing technique or high end paper. Will upload current design so you can see the logo and what we are using currently, but we want something more unique and elegant. I included our logo to help with design.

Target Market(s)

High end custom home buyers of $1.5 million plus homes. Also real estate developers of high end communities.

Industry/Entity Type

Business

Contact Information for Business Card

Double sided. We want something very elegant and expensive looking. We are looking to incorporate a combination of perhaps linen paper or a high end paper, with foil stamping or embossing/debossing to make the card look unique, but still elegant. We tend to use blacks and golds, but are open to any ideas. Looking for creative and unique design.

Colors

Designer to choose colors to be used in the design.

Requirements
Must have
• High end, elegant look. Can use foil, embossing, or high end papers like linen. We want to make the card unique and interesting, but elegant and expensive looking.
Nice to have
• I am including just some cards I saw that looked interesting for one reason or another. I like a clean elegant design and like both the clean white style, and the blacks. So not sure if we want a black design or white. Would like to see both.

```html
<!DOCTYPE html>
<html lang="en">
<head>
<meta charset="utf-8">
<title>Ridgecrest Custom Homes – Business Card</title>
<link rel="stylesheet" href="https://fonts.googleapis.com/css2?family=Montserrat:wght@400;500;600;700&display=swap">
<style>
  :root{
    --canvas:#e4e4e6;
    --paper:#ffffff;
    --ink:#0a0a0a;
    --gold-dark:#8a7a2c;
    --gold:#c9b84a;
    --gold-light:#e8e57a;
    --white:#ffffff;
  }
  *{margin:0;padding:0;box-sizing:border-box}
  html,body{width:1200px;height:1200px;overflow:hidden}
  body{
    background:var(--canvas);
    font-family:"Montserrat",sans-serif;
    position:relative;
  }
  .card{
    position:absolute;
    border-radius:22px;
    overflow:hidden;
    background:var(--paper);
  }
  .card-front{left:67px;top:417px;width:640px;height:366px}
  .card-back{left:767px;top:280px;width:366px;height:640px}

  .wordmark{
    display:flex;align-items:center;gap:12px;
    position:absolute;
    color:var(--ink);font-weight:600;letter-spacing:.08em;text-transform:uppercase;
    white-space:nowrap;
  }
  .wordmark-dot{border-radius:50%;background:var(--gold);flex:none}
  .card-front .wordmark{left:50%;top:50%;transform:translate(-50%,-50%);font-size:26px}
  .card-front .wordmark-dot{width:22px;height:22px}
  .card-back .wordmark{left:50%;top:150px;transform:translateX(-50%);font-size:15px;gap:8px}
  .card-back .wordmark-dot{width:13px;height:13px}

  .back-art{position:absolute;inset:0}

  .contact{position:absolute;left:28px;right:28px;bottom:20px;color:var(--white)}
  .person-name{font-size:22px;font-weight:700;letter-spacing:.01em;line-height:1}
  .person-title{font-size:14px;font-weight:600;letter-spacing:.06em;margin-top:4px;line-height:1.2}
  .rule{height:1.5px;background:linear-gradient(90deg,var(--gold-dark),var(--gold-light),var(--gold-dark));margin:8px 0}
  .row{display:flex;align-items:center;gap:14px;font-size:9.5px;font-weight:500;line-height:1.45}
  .icon{width:24px;height:24px;border-radius:50%;background:var(--white);flex:none;display:flex;align-items:center;justify-content:center}
  .icon svg{width:12px;height:12px}
  .social{display:flex;gap:10px;justify-content:flex-end;margin-top:4px}
  .social span{width:18px;height:18px;border-radius:4px;background:var(--white)}
</style>
</head>
<body>

<section class="card card-front" aria-label="Business card front">
  <div class="wordmark"><span class="wordmark-dot"></span>Ridgecrest Custom Homes</div>
</section>

<section class="card card-back" aria-label="Business card back">
  <svg class="back-art" viewBox="0 0 366 640" aria-hidden="true">
    <defs>
      <linearGradient id="goldSweep" x1="1" y1="0" x2="0" y2="1">
        <stop offset="0" stop-color="#8a7a2c"/>
        <stop offset=".45" stop-color="#e8e57a"/>
        <stop offset="1" stop-color="#8a7a2c"/>
      </linearGradient>
    </defs>
    <path d="M366,110 C352,280 200,360 0,378 L0,640 L366,640 Z" fill="url(#goldSweep)"/>
    <path d="M366,142 C345,295 205,375 0,392 L0,640 L366,640 Z" fill="#0a0a0a"/>
  </svg>

  <div class="wordmark"><span class="wordmark-dot"></span>Ridgecrest Custom Homes</div>

  <div class="contact">
    <div class="person-name">DEMO NAME</div>
    <div class="person-title">PRESIDENT</div>
    <div class="rule"></div>
    <div class="row">
      <span class="icon"><svg viewBox="0 0 12 12"><rect x="3.5" y="1" width="5" height="10" rx="1" fill="none" stroke="#0a0a0a" stroke-width="1.2"/></svg></span>
      <div>000 000 000<br>111 111 1111</div>
    </div>
    <div class="rule"></div>
    <div class="row">
      <span class="icon"><svg viewBox="0 0 12 12"><circle cx="6" cy="6" r="4.5" fill="none" stroke="#0a0a0a" stroke-width="1.2"/><path d="M1.5 6h9M6 1.5c2 2.5 2 6.5 0 9M6 1.5c-2 2.5-2 6.5 0 9" fill="none" stroke="#0a0a0a" stroke-width=".9"/></svg></span>
      <div>info@ridgecrestcustomhome.com.au<br>www.ridgecrestcustomhome.com.au</div>
    </div>
    <div class="rule"></div>
    <div class="row">
      <span class="icon"><svg viewBox="0 0 12 12"><path d="M6 11.2C3.6 8 2.4 6.2 2.4 4.6a3.6 3.6 0 0 1 7.2 0c0 1.6-1.2 3.4-3.6 6.6z" fill="#0a0a0a"/><circle cx="6" cy="4.6" r="1.3" fill="#fff"/></svg></span>
      <div>Unit 4 12-16 Harlow Street,<br>Bayview, WA 6102.</div>
    </div>
    <div class="rule"></div>
    <div class="social" aria-label="Social profiles">
      <span></span><span></span><span></span><span></span>
    </div>
  </div>
</section>

</body>
</html>
```